Simple and Clean business card design

We would like the design to be simple clean and to incorporate our colors.

We are open to your design and talent, we have the dots in our logo as we think of it as data points and we connect data points for people.

We are open to see the great creative and clean design you bring to the table

Contact Information for Business Card

please include: name, position, email, phone and website

Font styles to use
Sans Serif

Requirements
Must have
• my colors incorporated, simplicity
Nice to have
• lots of white space, simplicity
Should not have
• complexicity/ complex art

```html
<!DOCTYPE html>
<html lang="en">
<head>
<meta charset="UTF-8">
<title>Nodara – Business Card</title>
<link rel="stylesheet" href="https://fonts.googleapis.com/css2?family=Montserrat:wght@600&family=Work+Sans:wght@400;600&display=swap">
<style>
  :root {
    --backdrop: #d8d1c7;
    --card: #1d1c1f;
    --card-edge: #3a383c;
    --ink-light: #f1efec;
    --ink-soft: #d9d3cb;
    --name-blue: #4f7fcf;
    --accent-yellow: #e8b914;
    --icon: #9a948d;
  }
  html, body {
    margin: 0;
    width: 1200px;
    height: 887px;
    overflow: hidden;
    background: var(--backdrop);
  }
  .card {
    position: absolute;
    left: 100px;
    top: 170px;
    width: 1000px;
    height: 546px;
    background: var(--card);
    border: 2px solid var(--card-edge);
    border-radius: 26px;
    box-sizing: border-box;
    overflow: hidden;
    font-family: "Work Sans", sans-serif;
  }
  .accent-bar {
    position: absolute;
    left: 0;
    top: 246px;
    width: 18px;
    height: 60px;
    background: var(--accent-yellow);
  }
  .brand {
    position: absolute;
    left: 60px;
    top: 72px;
    margin: 0;
    font-family: "Work Sans", sans-serif;
    font-weight: 600;
    font-size: 86px;
    line-height: 1;
    letter-spacing: -1px;
    color: var(--ink-light);
  }
  .person {
    position: absolute;
    left: 60px;
    top: 242px;
  }
  .person-name {
    margin: 0;
    font-family: "Montserrat", sans-serif;
    font-weight: 600;
    font-size: 35px;
    letter-spacing: 2px;
    color: var(--name-blue);
    line-height: 1.1;
  }
  .person-role {
    margin: 4px 0 0;
    font-size: 24px;
    letter-spacing: 1px;
    color: var(--ink-soft);
  }
  .address {
    position: absolute;
    left: 60px;
    top: 324px;
    margin: 0;
    font-style: normal;
    font-size: 24px;
    line-height: 32px;
    letter-spacing: 1px;
    color: var(--ink-soft);
  }
  .contact-list {
    position: absolute;
    left: 56px;
    top: 404px;
    margin: 0;
    padding: 0;
    list-style: none;
    font-size: 24px;
    line-height: 32px;
    letter-spacing: 1px;
    color: var(--ink-soft);
  }
  .contact-list li {
    display: flex;
    align-items: center;
    gap: 8px;
  }
  .contact-icon {
    width: 16px;
    height: 16px;
    flex: none;
  }
</style>
</head>
<body>
  <section class="card">
    <div class="accent-bar"></div>
    <h1 class="brand">Nodara</h1>

    <div class="person">
      <p class="person-name">DANIEL HART</p>
      <p class="person-role">Founder</p>
    </div>

    <address class="address">418 Brookfield Lane<br>Alder Springs, TX 78014</address>

    <ul class="contact-list">
      <li>
        <svg class="contact-icon" viewBox="0 0 16 16" aria-hidden="true">
          <path d="M4 1.5 L6 5 L4.6 6.3 C5.4 8.2 7.6 10.5 9.7 11.4 L11 10 L14.5 12 L13 14.5 C7.5 14 2 8.5 1.5 3 Z" fill="var(--icon)"/>
        </svg>
        <span>0400 118 392</span>
      </li>
      <li>
        <svg class="contact-icon" viewBox="0 0 16 16" aria-hidden="true">
          <rect x="1.5" y="3.5" width="13" height="9" fill="none" stroke="var(--icon)" stroke-width="1.4"/>
          <path d="M1.5 3.5 L8 9 L14.5 3.5" fill="none" stroke="var(--icon)" stroke-width="1.4"/>
        </svg>
        <span>hello@nodaralabs.com</span>
      </li>
      <li>
        <svg class="contact-icon" viewBox="0 0 16 16" aria-hidden="true">
          <circle cx="8" cy="8" r="6.5" fill="none" stroke="var(--icon)" stroke-width="1.3"/>
          <ellipse cx="8" cy="8" rx="2.8" ry="6.5" fill="none" stroke="var(--icon)" stroke-width="1.1"/>
          <path d="M1.5 8 H14.5" stroke="var(--icon)" stroke-width="1.1"/>
        </svg>
        <span>www.nodaralabs.com</span>
      </li>
    </ul>
  </section>
</body>
</html>
```